Legal Journal cover - modern and sylish

We require a cover design for a new, modern and digital legal academic journal. Attached is our logo so you can get an idea of the feel. This academic journal will have several editions per year.Requirements for the cover design:-The feel of the cover is to be modern -In harmony with our logo-While staying uniform and set in its design,
Updates

Colors
ec1f27

Requirements
Must have
• 1) Colour. Each edition will use different colours. (So we will need the source files to be able to continue to do this)
• 2) An image section. We would like to be able to put in different image or photo with each edition. So we need to have a section, most likely in the shape of a strip, that can include a different image or photo each edition. This part is where we can put a different image in for each edition. So this section would need to be able to accommodate different types of images. It could be a single square. Or it could be a line (a strip) that an image or images.
• 3) A title for the edition and volume and number. Like this:
• Volume 34, No 2 (2016): Contemporary Issues in Criminal Law
• I have attached a range of journals I found online to serve as inspiration.

```html
<!DOCTYPE html>
<html lang="en">
<head>
<meta charset="utf-8">
<title>Law in Focus – Academic Journal of Law</title>
<link rel="stylesheet" href="https://fonts.googleapis.com/css2?family=Zilla+Slab:wght@700&family=Bodoni+Moda:wght@400&display=swap">
<style>
  :root {
    --backdrop: #3b3b3c;
    --spine: #0c0d0e;
    --spine-top: #1f2021;
    --cover: #2c2a76;
    --ink: #ecebe4;
    --sky-top: #3f68b8;
    --sky-bottom: #5f88cf;
  }
  html, body {
    margin: 0;
    padding: 0;
    width: 1200px;
    height: 1000px;
    overflow: hidden;
    background: var(--backdrop);
  }
  .cover {
    position: absolute;
    left: 281px;
    top: 50px;
    width: 636px;
    height: 900px;
    background: var(--cover);
    color: var(--ink);
  }
  .spine {
    position: absolute;
    left: 0;
    top: 0;
    width: 217px;
    height: 100%;
    background: linear-gradient(180deg, var(--spine-top), var(--spine) 60%);
  }
  .spine-title {
    position: absolute;
    left: 108px;
    top: 333px;
    transform: translate(-50%, -50%) rotate(-90deg);
    font-family: "Bodoni Moda", serif;
    font-weight: 400;
    font-size: 78px;
    line-height: 80px;
    letter-spacing: 2px;
    white-space: nowrap;
    text-align: left;
  }
  .imprint {
    position: absolute;
    left: 36px;
    bottom: 28px;
    font-family: "Zilla Slab", serif;
    font-weight: 700;
    font-size: 17px;
    letter-spacing: 1px;
  }
  .issue-meta {
    position: absolute;
    right: 36px;
    top: 34px;
    font-family: "Bodoni Moda", serif;
    font-size: 11px;
    text-align: right;
    line-height: 16px;
  }
  .issue-meta .fields span { margin-left: 30px; }
  .journal-title {
    position: absolute;
    left: 237px;
    top: 62px;
    margin: 0;
    font-family: "Zilla Slab", serif;
    font-weight: 700;
    font-size: 60px;
    line-height: 58px;
    letter-spacing: 1px;
  }
  .edition-image {
    position: absolute;
    left: 217px;
    top: 182px;
    width: 383px;
    height: 171px;
    background: linear-gradient(180deg, var(--sky-top), var(--sky-bottom));
  }
  .journal-subtitle {
    position: absolute;
    left: 237px;
    top: 356px;
    margin: 0;
    font-family: "Bodoni Moda", serif;
    font-weight: 400;
    font-size: 48px;
    line-height: 48px;
    letter-spacing: 1.5px;
  }
</style>
</head>
<body>
  <article class="cover">
    <aside class="spine">
      <div class="spine-title">LAW IN<br>FOCUS</div>
      <div class="imprint">LAW IN FOCUS</div>
    </aside>
    <div class="issue-meta">
      <div class="fields"><span>Volume</span><span>Month</span><span>Issue</span></div>
      <div>ISSN 0001</div>
    </div>
    <h1 class="journal-title">LAW IN<br>FOCUS</h1>
    <div class="edition-image" role="img" aria-label="Edition photograph: statue of Lady Justice with sword and scales against a blue sky"></div>
    <h2 class="journal-subtitle">ACADEMIC<br>JOURNAL<br>OF LAW</h2>
  </article>
</body>
</html>
```